Wordpress Design Job: Hosted PBX VoIP Web Site WordPress Template

We offer hosted 'in the cloud' telephone services. This is a new site for http://www.brellatone.com.au. The site Currently has a template upload but it is not suitable for a Hosted PBX. The site MUST BE be completed in WordPress as a template design.

I want this new site to have a warm look and feel giving the impression that we give the best customer service for small to medium businesses. The target business customer is small business with 5 to 50 employees with remote working employees who need to stay in communications with other staff.

Differentiation from our competitors is what we are looking for. We have been selling hosted pbx services and internet for more than 3 years, we own our data center and have been in the data center business since 2010. Here are some examples of what I would like to have as a new web site:

Other hosted PBX companies:
http://yourtradeline.com.au
http://zlinex.com.au
http://www.pormela.com/
http://www.gruvin.com/
http://www.talbrenix.com/
http://www.quorvel.com/
http://www.swiftlinq.com/
http://www.dubsel.com/

I will invest in good graphics and original photography and graphics as needed.

Colin Watts
http://www.hamvale.com.au

http://www.trade.qlr.com/content/mixedmedia/CallCore_H264.mp4 Watch this video. It tells what we do but on a smaller scale. We don't have the budget QL&R has to do what they did.

When needed I will engage http://www.wordplinth.com to write come fresh new content work our new web site. That is why it's important that it be a good WordPress template that I can add news articles to for good SEO.
I will add our proposed logo up on Monday - but am flexible if you have ideas of your own

Target Market(s)

small business owners, business with tele or remote workers

Industry/Entity Type

Small Business

Requirements
Must have
• Clean Look - Easy to read and naviagte

```html
<!DOCTYPE html>
<html lang="en">
<head>
<meta charset="utf-8">
<title>Brellatone – Hosted PBX</title>
<link href="https://fonts.googleapis.com/css2?family=Oswald:wght@300;400&family=Questrial&display=swap" rel="stylesheet">
<style>
:root{
  --blue:#1ea6f2;
  --blue-title:#1a8ad4;
  --blue-band:#1783d0;
  --blue-deep:#1470c0;
  --dark:#3d3d3d;
  --footer:#2b2b2b;
  --text:#555;
  --grey-band:#efefef;
  --line:#dcdcdc;
  --white:#fff;
}
*{margin:0;padding:0;box-sizing:border-box}
html,body{width:1200px;height:2239px;overflow:hidden}
body{position:relative;background:var(--white);font-family:'Questrial',sans-serif;color:var(--text)}
.abs{position:absolute}
.btn{position:absolute;background:var(--dark);color:var(--white);font-size:13px;letter-spacing:.3px;display:flex;align-items:center;justify-content:center;border-radius:2px}
p.body-text{font-size:12.5px;line-height:21.5px;text-align:center}

/* top bar */
.topbar{left:0;top:0;width:1200px;height:36px;background:var(--blue)}
.topbar .call{left:775px;top:9px;color:var(--white);font-size:14px;display:flex;align-items:center;gap:8px}
.topbar .auth{left:968px;top:10px;color:var(--white);font-size:12px}
.topbar .search{left:1077px;top:0;width:48px;height:36px;background:#1590dc;display:flex;align-items:center;justify-content:center}

/* header */
.header{left:0;top:36px;width:1200px;height:92px;background:linear-gradient(#fff,#ececec);border-bottom:1px solid #ddd}
.brand{left:75px;top:32px;display:flex;align-items:center;gap:8px;font-size:22px;color:var(--blue-deep)}
.brand .mark{width:16px;height:16px;border-radius:50%;background:var(--blue)}
.nav{top:44px;font-size:12.5px;color:#333;letter-spacing:.3px}

/* hero */
.hero{left:0;top:128px;width:1200px;height:430px;background:linear-gradient(100deg,#c9c1b4 0%,#e6e2dc 35%,#6e6e6e 60%,#2e2e2e 80%,#d8d2c8 100%)}
.hero-title{left:75px;top:234px;width:447px;height:60px;background:rgba(20,20,20,.85);color:var(--white);font-family:'Oswald',sans-serif;font-weight:300;font-size:34px;padding-left:15px;line-height:60px}
.hero-copy{left:75px;top:301px;width:447px;height:136px;background:rgba(20,20,20,.7);color:var(--white);font-size:20px;line-height:29px;padding:10px 16px}
.hero-cta{left:75px;top:439px;width:194px;height:58px;background:var(--blue);color:var(--white);font-family:'Oswald',sans-serif;font-size:24px;line-height:58px;padding-left:16px}
.hero-arrow{left:269px;top:439px;width:47px;height:58px;background:#111}

/* welcome */
.section-title{font-size:21px;color:var(--blue-title);letter-spacing:.3px}

/* services */
.band{left:0;top:830px;width:1200px;height:322px;background:linear-gradient(90deg,#1577c4,#2a9de6 40%,#1a84d2 70%,#38a6ea)}
.card{top:795px;width:240px;height:389px;background:var(--white);border:1px solid var(--line)}
.card .icon{position:absolute;left:75px;top:21px;width:90px;height:90px;border-radius:50%;background:var(--blue-deep);border:3px solid #cfe6f7;display:flex;align-items:center;justify-content:center}
.card h3{position:absolute;top:124px;width:100%;text-align:center;font-weight:400;font-size:15px;color:var(--blue-title)}
.card p{position:absolute;top:148px;left:28px;width:184px}
.card .btn{left:62px;top:332px;width:116px;height:40px}

/* why */
.grey{left:0;top:1213px;width:1200px;height:306px;background:var(--grey-band)}
.video{left:640px;top:1231px;width:485px;height:270px;border:3px solid #bbb;background:radial-gradient(circle at 45% 55%,#8a8a8a,#555 60%,#444)}
.controls{left:643px;top:1477px;width:479px;height:21px;background:#1c1c1c}

/* boxes */
.box{top:1549px;height:239px;border:1px solid var(--line);background:var(--white)}
.box h2{position:absolute;left:24px;top:22px;font-weight:400;font-size:21px;color:var(--blue-title)}
.post-img{width:63px;height:60px;background:linear-gradient(#777,#333)}
.post-title{font-size:14px;line-height:21px;color:var(--blue-title)}
.post-sub{font-size:12px;color:var(--text);margin-top:4px}

/* stories */
.stories{left:0;top:1818px;width:1200px;height:310px;background:var(--blue-band);color:var(--white)}
.dot{top:2087px;width:10px;height:10px;border-radius:50%;background:var(--white)}

/* footer */
.footer{left:0;top:2128px;width:1200px;height:111px;background:var(--footer)}
.social{top:2168px;width:30px;height:30px;border-radius:50%;background:var(--white)}
</style>
</head>
<body>

<div class="abs topbar">
  <div class="abs call">
    <svg width="14" height="14" viewBox="0 0 14 14"><rect width="14" height="14" rx="2" fill="#fff"/><path d="M4 3l2 2-1 1.2c.6 1.3 1.5 2.2 2.8 2.8L9 8l2 2-1.4 1.4C6.4 11 3 7.6 2.6 4.4z" fill="#1ea6f2"/></svg>
    Call Us: 123-555-0147
  </div>
  <div class="abs auth">Log In &nbsp;|&nbsp;Register</div>
  <div class="abs search"><svg width="14" height="14" viewBox="0 0 14 14"><circle cx="8.5" cy="5.5" r="4" fill="none" stroke="#fff" stroke-width="2"/><path d="M5.5 8.5L1.5 12.5" stroke="#fff" stroke-width="2.4"/></svg></div>
</div>

<div class="abs header">
  <div class="abs brand"><span class="mark"></span>Brellatone</div>
  <div class="abs nav" style="left:561px">HOME</div>
  <div class="abs nav" style="left:639px">ABOUT US</div>
  <div class="abs nav" style="left:742px">PRODUCTS</div>
  <div class="abs nav" style="left:849px">SUPPORT</div>
  <div class="abs nav" style="left:948px">PARTNERS</div>
  <div class="abs nav" style="left:1048px">CONTACT US</div>
</div>

<div class="abs hero" role="img" aria-label="Photo of an office desk phone with coiled handset cord beside a plant"></div>
<div class="abs hero-title">Nemo enim ipsam voluptatem</div>
<div class="abs hero-copy">Lorem ipsum dolor sit amet, consectetur adipisicing eitseo eiusmod tempor incididunt ut labore et dolore magna aliqua.</div>
<div class="abs hero-cta">TAKE A FREE TOUR</div>
<div class="abs hero-arrow"><svg width="47" height="58" viewBox="0 0 47 58"><path d="M17 12l14 10-14 9 14 10-14 9" fill="none" stroke="#fff" stroke-width="2"/></svg></div>

<div class="abs section-title" style="left:0;width:1200px;top:587px;text-align:center">WELCOME TO OUR WEBSITE</div>
<p class="abs body-text" style="left:75px;width:1050px;top:628px">Aliquam molestie, mi et imperdiet euismod, dui purus auctor tellus, et interdum lacus lectus et ante. Sed accumsan sollicitudin sapien, sit amet adipiscing turpis gravida ac. In congue, neque ac lobortis volutpat, libero mauris varius mi, vitae suscipit ipsum ligula vitae risus. Duis aliquam nibh a dui iaculis viverra id a velit. Vivamus egestas risus in magna varius commodo. Sed semper viverra egestas. Etiam pretium porttitor lectus, vel ornare neque porta volutpat.</p>
<div class="btn" style="left:542px;top:718px;width:116px;height:40px">READ MORE</div>

<div class="abs band"></div>

<div class="abs card" style="left:75px">
  <div class="icon"><svg width="50" height="44" viewBox="0 0 50 44"><path d="M12 36a10 10 0 0 1 0-20 14 14 0 0 1 27-3 11 11 0 0 1-1 23z" fill="#fff"/><path d="M20 16l4 4-2 2c1 2 3 4 5 5l2-2 4 4-3 3c-6-1-12-7-13-13z" fill="#1470c0"/></svg></div>
  <h3>HOSTED PBX</h3>
  <p class="body-text">Aliquam molestie, mi et imperdiet euismod, dui purus auctor tellus, et interdum lacus lectus et ante. Sed accumsan sollicitudin sapien, sit amet adipiscing turpis gravida ac. Vivamus egestas risus in magna varius ...</p>
  <div class="btn">READ MORE</div>
</div>
<div class="abs card" style="left:345px">
  <div class="icon"><svg width="50" height="44" viewBox="0 0 50 44"><circle cx="15" cy="11" r="6" fill="#fff"/><path d="M6 34l5-14h8l4 6" fill="none" stroke="#fff" stroke-width="5" stroke-linecap="round"/><path d="M22 36l16-16" stroke="#fff" stroke-width="5" stroke-linecap="round"/><circle cx="40" cy="17" r="6" fill="#fff"/><circle cx="42" cy="15" r="3" fill="#1470c0"/></svg></div>
  <h3>ONSITE MANAGED</h3>
  <p class="body-text">Aliquam molestie, mi et imperdiet euismod, dui purus auctor tellus, et interdum lacus lectus et ante. Sed accumsan sollicitudin sapien, sit amet adipiscing turpis gravida ac. Vivamus egestas risus in magna varius ...</p>
  <div class="btn">READ MORE</div>
</div>
<div class="abs card" style="left:615px">
  <div class="icon"><svg width="50" height="50" viewBox="0 0 50 50"><circle cx="25" cy="25" r="19" fill="#fff"/><path d="M14 16c5 1 7 4 5 8s2 6 0 10M30 10c-2 4 1 6 5 6s4 6 2 10c-3 4-6 6-5 12" fill="none" stroke="#1470c0" stroke-width="4"/></svg></div>
  <h3>VOIP</h3>
  <p class="body-text">Aliquam molestie, mi et imperdiet euismod, dui purus auctor tellus, et interdum lacus lectus et ante. Sed accumsan sollicitudin sapien, sit amet adipiscing turpis gravida ac. Vivamus egestas risus in magna varius ...</p>
  <div class="btn">READ MORE</div>
</div>
<div class="abs card" style="left:885px">
  <div class="icon"><svg width="52" height="50" viewBox="0 0 52 50"><circle cx="31" cy="20" r="11" fill="none" stroke="#fff" stroke-width="8" stroke-dasharray="5 3"/><circle cx="31" cy="20" r="8" fill="#fff"/><circle cx="31" cy="20" r="4" fill="#1470c0"/><circle cx="13" cy="37" r="6" fill="none" stroke="#fff" stroke-width="5" stroke-dasharray="3 2"/></svg></div>
  <h3>OTHER SERVICES</h3>
  <p class="body-text">Aliquam molestie, mi et imperdiet euismod, dui purus auctor tellus, et interdum lacus lectus et ante. Sed accumsan sollicitudin sapien, sit amet adipiscing turpis gravida ac. Vivamus egestas risus in magna varius ...</p>
  <div class="btn">READ MORE</div>
</div>

<div class="abs grey"></div>
<div class="abs section-title" style="left:75px;width:540px;top:1247px;text-align:center">WHY CHOOSE US?</div>
<p class="abs body-text" style="left:80px;width:540px;top:1282px">Aliquam molestie, mi et imperdiet euismod, dui purus auctor tellus, et interdum lacus lectus et ante. Sed accumsan sollicitudin sapien, sit amet adipiscing turpis gravida ac. In congue, neque ac lobortis volutpat, libero mauris varius mi, vitae suscipit ipsum ligula vitae risus. Duis aliquam nibh a dui iaculis viverra id a velit. Aenean a nibh eget turpis vehicula tempus ac sed massa. Vestibulum dolor nulla, ultrices ac tincidunt sed, laoreet non est. Suspendisse lobortis turpis in odio blandit ac interdum lorem euismod.</p>
<div class="btn" style="left:287px;top:1450px;width:116px;height:40px">READ MORE</div>

<div class="abs video" role="img" aria-label="Video still of a businessman using a phone, with an orange cloud and a make calls from any device caption"></div>
<svg class="abs" style="left:845px;top:1332px" width="78" height="78" viewBox="0 0 78 78"><circle cx="39" cy="39" r="35" fill="rgba(0,0,0,.25)" stroke="#fff" stroke-width="4"/><path d="M31 24l24 15-24 15z" fill="#fff"/></svg>
<div class="abs controls">
  <svg width="479" height="21" viewBox="0 0 479 21"><path d="M10 5l9 5.5-9 5.5z" fill="#ccc"/><rect x="40" y="9" width="310" height="3" fill="#555"/><rect x="40" y="9" width="65" height="3" fill="#aaa"/><circle cx="105" cy="10.5" r="5" fill="#ddd"/><text x="362" y="14.5" fill="#ccc" font-size="10" font-family="Questrial,sans-serif">0:30</text><path d="M392 8h3l4-3v11l-4-3h-3z" fill="#ccc"/><rect x="410" y="9" width="45" height="3" fill="#aaa"/><circle cx="453" cy="10.5" r="4" fill="#ddd"/><rect x="463" y="5" width="11" height="11" fill="none" stroke="#ccc" stroke-width="1.5"/></svg>
</div>

<div class="abs box" style="left:75px;width:509px">
  <h2>WHY CHOOSE US?</h2>
  <p class="abs" style="left:24px;top:58px;width:460px;font-size:12.5px;line-height:21.5px">Aliquam molestie, mi et imperdiet euismod, dui purus auctor tellus, et interdum lacus lectus et ante. Sed accumsan sollicitudin sapien, sit amet adipiscing turpis gravida ac. In congue, neque ac lobortis volutpat, libero mauris varius mi, vitae suscipit ipsum ligula vitae risus. Duis aliquam nibh a dui iaculis viverra id a velit.</p>
  <div class="btn" style="left:24px;top:176px;width:116px;height:40px">READ MORE</div>
</div>
<div class="abs box" style="left:615px;width:510px">
  <h2>BLOG POSTS</h2>
  <div class="abs post-img" style="left:26px;top:62px" role="img" aria-label="Close-up photo of phone keypad buttons"></div>
  <div class="abs" style="left:104px;top:58px;width:390px"><div class="post-title">Aliquam molestie, mi et imperdiet euismod, dui purus auctor tellus, et</div><div class="post-sub">Interdum lacus lectus et ante. Sed accumsan sollicitudin...</div></div>
  <div class="abs post-img" style="left:26px;top:156px;background:linear-gradient(#eee,#bbb)" role="img" aria-label="Photo of a woman talking on a phone"></div>
  <div class="abs" style="left:104px;top:151px;width:390px"><div class="post-title">Aliquam molestie, mi et imperdiet euismod, dui purus auctor tellus, et</div><div class="post-sub">Interdum lacus lectus et ante. Sed accumsan sollicitudin...</div></div>
</div>

<div class="abs stories">
  <div class="abs section-title" style="left:0;width:1200px;top:32px;text-align:center;color:var(--white)">CUSTOMER STORIES</div>
  <svg class="abs" style="left:75px;top:82px" width="1050" height="100" viewBox="0 0 1050 100"><path d="M.5 0v92.5h516l8 8 8-8h517V0" fill="none" stroke="#5fb2ea" stroke-width="1"/></svg>
  <p class="abs body-text" style="left:110px;width:980px;top:80px;color:#d7ecfb">Aliquam molestie, mi et imperdiet euismod, dui purus auctor tellus, et interdum lacus lectus et ante. Sed accumsan sollicitudin sapien, sit amet adipiscing turpis gravida ac. In congue, neque ac lobortis volutpat, libero mauris varius mi, vitae suscipit ipsum ligula vitae risus. Duis aliquam nibh a dui iaculis viverra id a velit. Vivamus egestas risus in magna varius commodo. Sed semper viverra egestas. Etiam pretium porttitor lectus, vel ornare neque porta volutpat.</p>
  <div class="abs" style="left:0;width:1200px;top:207px;text-align:center;font-size:13px">Rafe Dunmore</div>
  <div class="abs" style="left:0;width:1200px;top:226px;text-align:center;font-size:10.5px;color:#d7ecfb">A VAN 2-GO</div>
</div>
<div class="abs dot" style="left:576px;background:#111"></div>
<div class="abs dot" style="left:594px"></div>
<div class="abs dot" style="left:612px"></div>

<div class="abs footer">
  <div class="abs" style="left:75px;top:50px;font-size:11.5px;color:#999">Copyright © 2015 CompanyName. All rights reserved.</div>
  <div class="abs" style="left:884px;top:50px;font-size:12px;color:#fff">Connect Us:</div>
</div>
<div class="abs social" style="left:961px"></div>
<div class="abs social" style="left:995px"></div>
<div class="abs social" style="left:1029px"></div>
<div class="abs social" style="left:1063px"></div>
<div class="abs social" style="left:1097px"></div>

</body>
</html>
```